In Home Senior Care Agency Business Card Design Needed

At Silver Birch Helpers, we don't just work in the care-giving industry. We truly care.

We are dedicated to providing personable, hands-on and integrated caring services that aim to help people maintain safe and comfortable life standards within the familiar settings of their own homes.

We would like to see designs that use my logo colors obviously. The final design will be modern, yet professional and semi-minimalistic. It should communicate an well-established company that is innovative. We would also like the design to have that 'flat' design look. Ideally having the design roll over to the backend of the card. Most likely it will be printed on a Matte paper with a die cut (either 2 rounded corners -leaf cut) or all rounded.

Target Market(s)

Baby boomer generation. 45 years and older.

Industry/Entity Type

Business

Contact Information for Business Card

Text for Front:
Slogan somewhere "Our Family. Caring For Yours.”

Darren Whitlow
President

Cell: 917.284.6051
Phone: 917.512.7368
E: Darren@silverbirchhelpers.com
W: www.SilverBirchHelpers.com

Back:
-Meal Preparation
-Transportation
-Light Housekeeping
-Bathing Assistance
-Companionship

Font styles to use
Serif
Sans Serif

Requirements
Must have
• Flat, modern, professional design. Not too many colors. Match my colors in logo. Design of card must reflect from the front onto the back. Evenly spaced font.
Nice to have
• Try to work off current logo scheme, but logo may need to be redesigned.
Should not have
• Not too many colors.

```html
<!DOCTYPE html>
<html lang="en">
<head>
<meta charset="utf-8">
<title>Silver Birch Helpers – Business Card</title>
<link href="https://fonts.googleapis.com/css2?family=Open+Sans:wght@400;600;700&family=Lora:ital@1&display=swap" rel="stylesheet">
<style>
  :root{
    --backdrop:#e9e6e1;
    --card:#f4f4f3;
    --olive:#7d6c3c;
    --orange:#f2a22c;
    --brand-green:#1f7a3c;
    --ink:#3a3a3a;
    --muted:#6b6b6b;
    --white:#ffffff;
  }
  *{box-sizing:border-box;margin:0;padding:0}
  html,body{width:1200px;height:894px;overflow:hidden}
  body{background:var(--backdrop);font-family:"Open Sans",Arial,sans-serif;position:relative}

  .card{
    position:absolute;top:150px;width:340px;height:594px;
    background:var(--card);border-radius:24px;overflow:hidden;
    box-shadow:0 6px 18px rgba(0,0,0,.12);
  }
  .card--back{left:230px}
  .card--front{left:630px}

  .brand{display:flex;align-items:center;justify-content:center;gap:10px;color:var(--brand-green);
    font-weight:600;font-size:22px;letter-spacing:.2px;white-space:nowrap}
  .brand__dot{width:18px;height:18px;border-radius:50%;background:var(--orange);flex:none}

  .back-content{position:absolute;left:0;right:0;top:190px;text-align:center}
  .slogan{font-family:"Lora",Georgia,serif;font-style:italic;font-size:15px;color:var(--olive);margin-top:14px}
  .rule{width:60px;height:2px;background:var(--orange);margin:26px auto 22px}
  .services{list-style:none;font-size:13px;letter-spacing:1.2px;text-transform:uppercase;color:var(--ink)}
  .services li{line-height:30px}

  .card--front .brand{position:absolute;left:0;right:0;top:60px}

  .name-band{
    position:absolute;left:0;top:150px;width:262px;height:76px;
    background:var(--olive);border-radius:0 38px 38px 0;
    padding:14px 0 0 28px;color:var(--white);
  }
  .name-band__name{font-weight:700;font-size:20px;letter-spacing:.8px;text-transform:uppercase}
  .name-band__title{font-size:12px;letter-spacing:1.4px;text-transform:uppercase;margin-top:2px}

  .contacts{position:absolute;left:28px;right:16px;top:262px;list-style:none}
  .contacts li{display:flex;align-items:center;gap:10px;height:38px;
    font-size:12px;color:var(--ink);letter-spacing:.3px;text-transform:uppercase;white-space:nowrap}
  .contacts li.two-line{height:auto;align-items:flex-start;padding-top:9px;line-height:1.5}
  .contacts svg{flex:none}
  .contacts__label{font-weight:700;color:var(--olive)}

  .foot-band{position:absolute;left:0;right:0;bottom:0;height:34px;background:var(--olive)}
</style>
</head>
<body>

  <div class="card card--back">
    <div class="back-content">
      <div class="brand"><span class="brand__dot"></span>Silver Birch Helpers</div>
      <p class="slogan">“Our Family. Caring For Yours.”</p>
      <div class="rule"></div>
      <ul class="services">
        <li>Meal Preparation</li>
        <li>Transportation</li>
        <li>Light Housekeeping</li>
        <li>Bathing Assistance</li>
        <li>Companionship</li>
      </ul>
    </div>
  </div>

  <div class="card card--front">
    <div class="brand"><span class="brand__dot"></span>Silver Birch Helpers</div>

    <div class="name-band">
      <div class="name-band__name">Darren Whitlow</div>
      <div class="name-band__title">President</div>
    </div>

    <ul class="contacts">
      <li>
        <svg width="20" height="20" viewBox="0 0 20 20" aria-hidden="true"><circle cx="10" cy="10" r="8.5" fill="none" stroke="var(--orange)" stroke-width="1.6"/><path d="M7 6.5c0 4 2.5 6.5 6.5 6.5l.6-1.6-1.8-.9-.8.9c-1.2-.5-2-1.3-2.5-2.5l.9-.8-.9-1.8z" fill="var(--orange)"/></svg>
        <span><span class="contacts__label">Cell:</span> 917.284.6051</span>
      </li>
      <li>
        <svg width="20" height="20" viewBox="0 0 20 20" aria-hidden="true"><circle cx="10" cy="10" r="8.5" fill="none" stroke="var(--orange)" stroke-width="1.6"/><path d="M7 6.5c0 4 2.5 6.5 6.5 6.5l.6-1.6-1.8-.9-.8.9c-1.2-.5-2-1.3-2.5-2.5l.9-.8-.9-1.8z" fill="var(--orange)"/></svg>
        <span><span class="contacts__label">Phone:</span> 917.512.7368</span>
      </li>
      <li>
        <svg width="20" height="20" viewBox="0 0 20 20" aria-hidden="true"><circle cx="10" cy="10" r="9" fill="var(--orange)"/><rect x="5.5" y="7" width="9" height="6.5" fill="none" stroke="var(--white)" stroke-width="1.2"/><path d="M5.5 7l4.5 3.5L14.5 7" fill="none" stroke="var(--white)" stroke-width="1.2"/></svg>
        Darren@silverbirchhelpers.com
      </li>
      <li>
        <svg width="20" height="20" viewBox="0 0 20 20" aria-hidden="true"><circle cx="10" cy="10" r="9" fill="var(--orange)"/><circle cx="10" cy="10" r="4.5" fill="none" stroke="var(--white)" stroke-width="1.2"/><path d="M5.5 10h9M10 5.5c-2 3-2 6 0 9M10 5.5c2 3 2 6 0 9" fill="none" stroke="var(--white)" stroke-width="1"/></svg>
        www.SilverBirchHelpers.com
      </li>
      <li class="two-line">
        <svg width="20" height="20" viewBox="0 0 20 20" aria-hidden="true"><circle cx="10" cy="10" r="9" fill="var(--orange)"/><path d="M10 15s-3.5-3.6-3.5-6a3.5 3.5 0 0 1 7 0c0 2.4-3.5 6-3.5 6z" fill="var(--white)"/><circle cx="10" cy="9" r="1.2" fill="var(--orange)"/></svg>
        <span>48 Alder Lane,<br>Brookfield, USA</span>
      </li>
    </ul>

    <div class="foot-band"></div>
  </div>

</body>
</html>
```